Email graphic design for a survey

We have built a survey on Formly Nest and require someone who can develop some graphics in the email that will be sent in the first instance.
Target: Australia Wide, A
Offer: Opportunity to win 3 hours of one-to-one career coaching to responders as a prize draw
Email Creative Recommendations:
• A good text to image ratio
• Simple, but effective image based email which outlines both the inclusions of the survey and the one-to-one coaching prize
• Mobile and tablet responsive
• Refer to attached examples for one of our clients - Copper Lane Surveys
Landing Page: As supplied - https://www.formlynest.com/r/brindlewick Mobile and tablet responsive
Thank you for your submissions
Target Market(s)
ages 25-60 years old, white collar workers targeted
Other font styles liked:
- ubuntu

```html
<!DOCTYPE html>
<html lang="en">
<head>
<meta charset="utf-8">
<title>Brindlewick Surveys – Career Coaching Prize</title>
<link rel="stylesheet" href="https://fonts.googleapis.com/css2?family=Ubuntu:wght@400;500;700&display=swap">
<style>
  :root {
    --page-bg: #c9c9c9;
    --orange: #f58220;
    --blue: #0aa5df;
    --blue-deep: #0a8fc4;
    --ink: #111111;
    --white: #ffffff;
    --charcoal: #3a3f47;
    --photo-dark: #5d5a57;
    --photo-light: #e9e7e4;
  }
  * { box-sizing: border-box; margin: 0; padding: 0; }
  html, body { width: 1200px; height: 1200px; overflow: hidden; }
  body {
    background: var(--page-bg);
    font-family: "Ubuntu", sans-serif;
    color: var(--ink);
  }
  .email {
    position: absolute;
    left: 308px; top: 0;
    width: 584px; height: 1200px;
    background: var(--white);
    overflow: hidden;
  }
  .masthead {
    position: absolute; left: 0; top: 0; width: 100%; height: 75px;
    background: var(--orange);
  }
  .masthead__brand {
    position: absolute; left: 30px; top: 20px;
    color: var(--white); font-weight: 700; font-size: 28px; letter-spacing: 0.2px;
  }
  .hero {
    position: absolute; left: 0; top: 75px; width: 100%; height: 211px;
  }
  .hero__photo {
    position: absolute; inset: 0;
    background: linear-gradient(100deg, var(--photo-dark) 0%, #8a8784 38%, #cfccc8 62%, var(--photo-light) 100%);
  }
  .hero__title {
    position: absolute; left: 35px; top: 36px; color: var(--white);
    font-weight: 700; line-height: 1;
  }
  .hero__hours { font-size: 37px; display: block; }
  .hero__sub { font-size: 23px; display: block; line-height: 1.05; margin-top: 3px; }
  .hero__cta {
    position: absolute; left: 38px; top: 152px; width: 213px; height: 47px;
    background: var(--blue); color: var(--white);
    font-size: 30px; font-weight: 500;
    display: flex; align-items: center; justify-content: center; gap: 8px;
  }
  .greeting {
    position: absolute; left: 52px; top: 305px; width: 440px;
    font-size: 16px; line-height: 22px;
  }
  .greeting p + p { margin-top: 22px; }
  .incentive {
    position: absolute; left: 0; width: 100%; height: 91px;
  }
  .incentive--one { top: 436px; }
  .incentive--two { top: 531px; }
  .incentive__banner { position: absolute; left: 0; top: 0; }
  .incentive__text {
    position: absolute; left: 52px; top: 50%; transform: translateY(-50%);
    width: 320px; color: var(--white); font-size: 16px; line-height: 22px;
  }
  .incentive__badge {
    position: absolute; left: 438px; top: 2px; width: 88px; height: 88px;
    border: 5px solid var(--blue); border-radius: 50%; background: var(--white);
    display: flex; align-items: center; justify-content: center;
    font-weight: 700; font-size: 40px;
  }
  .steps {
    position: absolute; left: 0; top: 662px; width: 100%; height: 206px;
    background: var(--blue); color: var(--white);
  }
  .steps__title {
    position: absolute; top: 14px; width: 100%; text-align: center;
    font-size: 25px; font-weight: 500;
  }
  .step {
    position: absolute; top: 70px; width: 150px; text-align: center;
  }
  .step svg { display: block; margin: 0 auto; }
  .step__label {
    margin-top: 12px; font-size: 11px; font-weight: 700; line-height: 13px;
    text-transform: uppercase;
  }
  .closing { position: absolute; left: 0; top: 868px; width: 100%; height: 198px; }
  .closing__disc {
    position: absolute; left: 22px; top: 40px; width: 136px; height: 136px;
    border-radius: 50%; background: var(--charcoal);
  }
  .closing__heading {
    position: absolute; right: 42px; top: 26px; font-size: 17px; font-weight: 700;
  }
  .closing__body {
    position: absolute; left: 273px; top: 60px; width: 270px;
    font-size: 17px; line-height: 19px;
  }
  .closing__cta {
    position: absolute; left: 289px; top: 121px; width: 212px; height: 46px;
    background: var(--blue); color: var(--white); font-size: 19px; font-weight: 700;
    display: flex; align-items: center; justify-content: center; gap: 4px;
  }
  .footer {
    position: absolute; left: 0; top: 1066px; width: 100%; height: 134px;
    background: var(--orange); color: var(--white);
    font-size: 19px; font-weight: 700; text-align: center; padding-top: 40px;
  }
</style>
</head>
<body>
<main class="email">
  <header class="masthead">
    <div class="masthead__brand">Brindlewick Surveys</div>
  </header>

  <section class="hero">
    <div class="hero__photo" role="img" aria-label="Photo of a person writing in a spiral notebook beside a laptop"></div>
    <h1 class="hero__title">
      <span class="hero__hours">3 hours</span>
      <span class="hero__sub">of one-to-one<br>career coaching</span>
    </h1>
    <div class="hero__cta">Win it
      <svg width="18" height="20" viewBox="0 0 18 20"><path d="M0 0 L18 10 L0 20 Z" fill="#fff"/></svg>
    </div>
  </section>

  <section class="greeting">
    <p>Hi (First Name),</p>
    <p>Joint the Brindlewick Surveys Panel and in return for you offering your opinions to help organisations get feedback on their products.</p>
  </section>

  <section class="incentive incentive--one">
    <svg class="incentive__banner" width="440" height="91" viewBox="0 0 440 91"><path d="M0 0 H394 L440 45.5 L394 91 H0 Z" fill="var(--blue)"/></svg>
    <p class="incentive__text">You will <strong>receive a $3 incentive</strong> to your account when you register.</p>
    <div class="incentive__badge">$3</div>
  </section>

  <section class="incentive incentive--two">
    <svg class="incentive__banner" width="440" height="91" viewBox="0 0 440 91"><path d="M0 0 H394 L440 45.5 L394 91 H0 Z" fill="var(--blue)"/></svg>
    <p class="incentive__text">In additional to this, you will receive an <strong>additional $2</strong> when you update some basic profile questions.</p>
    <div class="incentive__badge">$2</div>
  </section>

  <section class="steps">
    <h2 class="steps__title">HOW TO WIN IT</h2>
    <div class="step" style="left:51px">
      <svg width="70" height="66" viewBox="0 0 70 66" fill="none" stroke="#fff" stroke-width="3.5">
        <path d="M38 10 A28 28 0 1 0 60 34"/>
        <path d="M42 4 h10 v12 h12 v10 h-12 v12 h-10 v-12 h-12 v-10 h12 Z" fill="var(--blue)"/>
      </svg>
      <p class="step__label">Sign up to<br>Brindlewick Surveys</p>
    </div>
    <div class="step" style="left:217px">
      <svg width="70" height="66" viewBox="0 0 70 66" fill="none" stroke="#fff" stroke-width="3.5">
        <path d="M42 9 A28 28 0 1 0 60 30"/>
        <path d="M56 2 L66 12 L40 38 L28 42 L32 30 Z" fill="var(--blue)"/>
        <path d="M50 8 L60 18"/>
      </svg>
      <p class="step__label">Start completing<br>surveys</p>
    </div>
    <div class="step" style="left:384px">
      <svg width="70" height="66" viewBox="0 0 70 66" fill="none" stroke="#fff" stroke-width="3.5">
        <path d="M34 10 A28 28 0 1 0 58 26"/>
        <text x="40" y="30" fill="#fff" stroke="none" font-family="Ubuntu, sans-serif" font-weight="700" font-size="30">$</text>
      </svg>
      <p class="step__label">Earn cash</p>
    </div>
  </section>

  <section class="closing">
    <div class="closing__disc"></div>
    <h3 class="closing__heading">What are you waiting for?</h3>
    <p class="closing__body">Register today and start earning money with Brindlewick Surveys</p>
    <div class="closing__cta">START EARNING
      <svg width="13" height="15" viewBox="0 0 13 15"><path d="M0 0 L13 7.5 L0 15 Z" fill="#fff"/></svg>
    </div>
  </section>

  <footer class="footer">BRINDLEWICK SURVEYS</footer>
</main>
</body>
</html>
```